Label and logo design for an all natural organic skincare product

We need a label design for a new company in the natural beauty space. The company is called "Vessa Kell". "Vessa" refers to the olive tree. "Kell" symbolizes the wren bird. The company name represents purity, nature, and freedom.

Our first product is tamanu oil - a 100% pure, organic, unrefined, cold pressed oil that is be used to improve various skin conditions (acne, eczema, scars, anti-aging) hair, and nails. Tamanu oil is a wonderful skin care healing agent that fades scars, rejuvenates skin cells, and is a powerful natural anti-aging product.

We currently do not have a company logo. We would like the logo and label to be designed together for a coordinated, well thought out, look.

We are looking for a label and logo that convey a high end quality product. We use premium quality all natural ingredients only.

Label size is 10.2cm (wide) x 4.5cm (height). The label wraps around a small amber colored glass bottle with a dropper similar to the images attached. The bottle holds 1oz (30ml) of oil.

Label will contain:
- Company logo
- Product name - "100% Pure Organic Tamanu Oil"
- Quantity - "1 fl oz / 30 ml"
- Ingredients - "100% pure virgin organic cold pressed tamanu oil (calophyllum inophyllum)
- Product Usage - "Dab a few drops of Vessa Kell tamanu oil into your hands and rub the oil into your skin or hair 1 - 3 times a day."
- UPC barcode - will provide later
- Company info:
"Vessa Kell
Atlanta, GA
www.vessakell.example"
- Warning - "For external use only. Do not use if you have allergies to nuts of any kind. Keep out of reach of children."

We've attached a couple images of labels that we like. In general, we prefer a modern, minimalistic, pure look but we are open to your ideas and creativity.

Colors we like: blue-green (think torquoise or tiffany blue), green, grey, white.

If you have any questions, about the design please let me know. The winning designer will be required to do a few additional tweaks to finalize the product. Thank you for your time and happy designing!

```html
<!DOCTYPE html>
<html lang="en">
<head>
<meta charset="utf-8">
<title>Vessa Kell Tamanu Oil – Packaging and Label</title>
<link rel="stylesheet" href="https://fonts.googleapis.com/css2?family=Cinzel:wght@400&family=Federo&family=Lora:ital@1&family=Open+Sans:wght@400;600&family=Oswald:wght@300&display=swap">
<style>
  :root {
    --bg: #e9e9ea;
    --paper: #ffffff;
    --ink: #4a4a4a;
    --ink-soft: #5c5c5c;
    --teal: #21b3ab;
    --leaf: #8fae2e;
    --silver-1: #f4f4f4;
    --silver-2: #a9a9a9;
    --silver-3: #6f6f6f;
    --logo-ring: #d9d9d9;
  }
  * { margin: 0; padding: 0; box-sizing: border-box; }
  html, body { width: 1200px; height: 935px; overflow: hidden; }
  body {
    background: var(--bg);
    font-family: "Open Sans", sans-serif;
    color: var(--ink);
    position: relative;
  }
  .panel {
    position: absolute;
    background: var(--paper);
    box-shadow: 0 2px 10px rgba(0,0,0,.08);
  }

  /* Box side panel */
  .box-side {
    left: 120px; top: 170px; width: 200px; height: 600px;
    padding: 60px 22px 0 22px;
  }
  .box-side .blurb {
    font-family: "Oswald", sans-serif;
    font-weight: 300;
    font-size: 15px;
    line-height: 1.55;
    color: var(--ink);
  }

  /* Box front panel */
  .box-front {
    left: 320px; top: 170px; width: 300px; height: 600px;
    text-align: center;
    padding-top: 50px;
  }
  .silver-band {
    position: absolute; left: 0; right: 0; bottom: 0; height: 70px;
    background: linear-gradient(180deg, var(--silver-1) 0%, var(--silver-2) 45%, var(--silver-1) 70%, var(--silver-3) 100%);
  }
  .box-side .silver-band { left: 0; }

  /* Brand */
  .brand { display: flex; flex-direction: column; align-items: center; }
  .brand-dot {
    width: 70px; height: 70px; border-radius: 50%;
    background: var(--paper);
    border: 2px solid var(--logo-ring);
    box-shadow: 0 1px 4px rgba(0,0,0,.12);
  }
  .brand-name {
    font-family: "Open Sans", sans-serif;
    font-size: 12px; font-weight: 400; color: var(--ink);
    margin-top: 6px;
  }

  .claim {
    font-family: "Federo", sans-serif;
    font-size: 23px; color: var(--ink-soft);
    margin-top: 34px;
  }
  .product {
    font-family: "Cinzel", serif;
    font-size: 32px; color: var(--ink);
    margin-top: 2px;
  }
  .tagline {
    font-family: "Lora", serif; font-style: italic;
    font-size: 19px; color: var(--leaf);
    margin-top: 26px;
  }
  .serum-band {
    background: var(--teal); color: var(--paper);
    font-size: 21px; padding: 8px 0;
    margin: 10px 0 0 22px;
  }
  .benefits {
    font-size: 16px; font-style: italic; line-height: 1.35;
    color: var(--ink-soft);
    margin-top: 50px;
  }
  .quantity {
    position: absolute; left: 0; right: 0; bottom: 88px;
    font-family: "Oswald", sans-serif; font-weight: 300;
    font-size: 15px; color: var(--ink);
  }

  /* Bottle label (front face) */
  .bottle-label {
    left: 720px; top: 250px; width: 330px; height: 440px;
    text-align: center; padding-top: 40px;
  }
  .bottle-label .claim { font-size: 22px; margin-top: 26px; }
  .bottle-label .product { font-size: 30px; }
  .bottle-label .tagline { font-size: 19px; margin-top: 16px; }
  .bottle-label .serum-band {
    display: inline-block; font-size: 18px; padding: 6px 22px; margin: 16px 0 0 0;
  }
  .bottle-label .silver-band { height: 46px; }
  .bottle-label .quantity { bottom: 58px; font-size: 13px; }
</style>
</head>
<body>

  <section class="panel box-side">
    <p class="blurb">Tamanu oil is a 100% pure, organic, unrefined, cold pressed oil that is be used to improve various skin conditions (acne, eczema, scars, anti-aging) hair and nails. Tamanu oil is a wonderful skin care healing agent that fades scars, rejuvenates skin cells, and is a powerful natural anti-aging product.</p>
    <div class="silver-band"></div>
  </section>

  <section class="panel box-front">
    <div class="brand">
      <span class="brand-dot"></span>
      <span class="brand-name">Vessa Kell</span>
    </div>
    <p class="claim">100% Pure Organic</p>
    <h1 class="product">TAMANU OIL</h1>
    <p class="tagline">Natural Skin Care</p>
    <p class="serum-band">Anti Aging Serum</p>
    <p class="benefits">•acne•eczema•scars•<br>•good for hair•nails<br>•rejuvenates skin cells•</p>
    <p class="quantity">1 fl oz / 30 ml</p>
    <div class="silver-band"></div>
  </section>

  <section class="panel bottle-label">
    <div class="brand">
      <span class="brand-dot"></span>
      <span class="brand-name">Vessa Kell</span>
    </div>
    <p class="claim">100% Pure Organic</p>
    <h2 class="product">TAMANU OIL</h2>
    <p class="tagline">Natural Skin Care</p>
    <p class="serum-band">Anti Aging Serum</p>
    <p class="quantity">1 fl oz / 30 ml</p>
    <div class="silver-band"></div>
  </section>

</body>
</html>
```